Verostel business card

Business card for sustainable investment company called "Verostel". Verostel is an exchange platform selling carbon credits between buyers and sellers. Carbon Credits are an environmental commodity for reducing global carbon emissions.

the card should obviously have our logo and the theme should be sustainability/environment mixed with a trading platform.

Contact Information for Business Card

Logo, Name, Title, Phone, Email

Colors
0054AA
0677BA
7BADD7
CADEEF
E8F1F8
0094D4
00A9DD
6FCCEA
C7EBF8
E9F6FB
00AB8E
00BBA5
67D7C9
C6EFE9
E9F9F6
59FF00
82FF00
B8FF75
E3FFCB
F4FFEA

```html
<!DOCTYPE html>
<html lang="en">
<head>
<meta charset="utf-8">
<title>Verostel Business Card</title>
<link href="https://fonts.googleapis.com/css2?family=Raleway:wght@400;500;600&display=swap" rel="stylesheet">
<style>
  :root {
    --backdrop: #e9e9e9;
    --card: #ffffff;
    --brand-blue: #00a9dd;
    --brand-sky: #6fccea;
    --brand-pale: #c7ebf8;
    --brand-mist: #e9f6fb;
    --ink: #1b2b4b;
  }
  * { margin: 0; padding: 0; box-sizing: border-box; }
  html, body {
    width: 1200px; height: 900px; overflow: hidden;
    background: var(--backdrop);
    font-family: "Raleway", sans-serif;
  }
  .card {
    position: absolute; left: 150px; top: 170px;
    width: 900px; height: 560px;
    background: var(--card);
    overflow: hidden;
    box-shadow: 0 18px 40px rgba(0,0,0,0.18);
  }
  .card-shapes { position: absolute; inset: 0; }
  .brand-name {
    position: absolute; left: 60px; top: 120px; width: 270px;
    text-align: center;
    color: #fff; font-weight: 600; font-size: 44px; letter-spacing: 1px;
  }
  .holder {
    position: absolute; left: 560px; top: 52px; width: 310px;
    text-align: right; color: var(--ink);
  }
  .holder-name {
    font-weight: 500; font-size: 42px; letter-spacing: -0.5px;
    padding-bottom: 4px;
    border-bottom: 3px solid var(--ink);
  }
  .holder-title {
    margin-top: 6px; font-weight: 500; font-size: 16px;
    letter-spacing: 11px; text-align: center; padding-left: 60px;
  }
  .contact {
    position: absolute; left: 378px; top: 272px;
    padding-left: 22px; border-left: 4px solid var(--ink);
    color: var(--ink); list-style: none;
  }
  .contact-item {
    display: flex; align-items: center; gap: 16px;
    font-size: 28px; font-weight: 500; line-height: 48px;
  }
  .contact-icon { width: 26px; height: 26px; fill: var(--ink); flex: none; }
</style>
</head>
<body>
  <article class="card">
    <svg class="card-shapes" viewBox="0 0 900 560" aria-hidden="true">
      <polygon points="30,560 195,365 410,560" fill="var(--brand-mist)"/>
      <polygon points="42,560 210,385 365,560" fill="var(--brand-pale)"/>
      <polygon points="507,0 538,0 42,560 15,560" fill="var(--brand-sky)"/>
      <polygon points="0,0 507,0 15,560 0,560" fill="var(--brand-blue)"/>
    </svg>

    <div class="brand-name">VEROSTEL</div>

    <header class="holder">
      <div class="holder-name">YOUR NAME</div>
      <div class="holder-title">TAGLINE</div>
    </header>

    <ul class="contact">
      <li class="contact-item">
        <svg class="contact-icon" viewBox="0 0 24 24"><path d="M2 5h20v14H2z M3 6l9 7 9-7" fill="none" stroke="currentColor"/><path d="M2 5h20v2l-10 7L2 7z M2 9l6 4.5L2 18z M22 9l-6 4.5L22 18z M9 14.5l3 2 3-2 6 4.5H3z"/></svg>
        yourname@verostel.com
      </li>
      <li class="contact-item">
        <svg class="contact-icon" viewBox="0 0 24 24"><path d="M6.6 10.8c1.4 2.8 3.8 5.1 6.6 6.6l2.2-2.2c.3-.3.7-.4 1-.2 1.1.4 2.3.6 3.6.6.6 0 1 .4 1 1V20c0 .6-.4 1-1 1C10.6 21 3 13.4 3 4c0-.6.4-1 1-1h3.5c.6 0 1 .4 1 1 0 1.3.2 2.5.6 3.6.1.3 0 .7-.2 1z"/></svg>
        000-000-0000
      </li>
      <li class="contact-item">
        <svg class="contact-icon" viewBox="0 0 24 24"><path d="M12 2C8.1 2 5 5.1 5 9c0 5.2 7 13 7 13s7-7.8 7-13c0-3.9-3.1-7-7-7zm0 9.5a2.5 2.5 0 1 1 0-5 2.5 2.5 0 0 1 0 5z"/></svg>
        32/64 your location
      </li>
    </ul>
  </article>
</body>
</html>
```